Modern Billboard Ad for Criminal Defense Firm

10.5 x 36 We're looking for something to set us apart from the local competition. Looking for sleek and modern. We're a mid-sized firm in a small market city. We want to give the artist room to be creative on this one.
Thanks

Target Market(s)

Adult clients who have been charged with a crime/DWI

Industry/Entity Type

legal

Font styles to use
Serif
Sans Serif

Requirements
Must have
• Needs to have the firm name in large lettering. Law Offices of Martin G Ashby. “PLLC” does not have to be included. Phone number of (555) 318-4092 should be included but not the main focus.
Nice to have
• A call to action or something similar. “Don’t go it alone, call today.”, “ Arrested?”

```html
<!DOCTYPE html>
<html lang="en">
<head>
<meta charset="utf-8">
<title>Martin G Ashby Billboard</title>
<link href="https://fonts.googleapis.com/css2?family=Montserrat:wght@500;600;700&display=swap" rel="stylesheet">
<style>
  :root {
    --navy: #111a28;
    --navy-deep: #0e1622;
    --gold-rule: #efe08a;
    --cta-yellow: #f4e04d;
    --white: #ffffff;
    --page: #ffffff;
    --badge-blue: #2a9fd8;
    --badge-dark: #1c2633;
  }
  html, body {
    margin: 0;
    padding: 0;
    width: 1059px;
    height: 1200px;
    overflow: hidden;
    background: var(--page);
  }
  .canvas {
    position: relative;
    width: 1059px;
    height: 1200px;
  }
  .billboard {
    position: absolute;
    left: 22px;
    top: 459px;
    width: 1014px;
    height: 282px;
    background: var(--navy);
    display: flex;
    font-family: "Montserrat", sans-serif;
    color: var(--white);
  }
  .portrait {
    width: 232px;
    height: 100%;
    background: linear-gradient(160deg, #1a2433 0%, #3c4654 45%, #8a929c 100%);
  }
  .rule-vertical {
    width: 2px;
    height: 100%;
    background: var(--gold-rule);
  }
  .firm-panel {
    width: 546px;
    height: 100%;
    display: flex;
    flex-direction: column;
    align-items: center;
    text-align: center;
  }
  .firm-lead {
    margin: 34px 0 0;
    font-size: 44px;
    font-weight: 500;
    line-height: 1;
    letter-spacing: 0.5px;
  }
  .firm-of {
    display: flex;
    align-items: center;
    gap: 8px;
    margin-top: 14px;
    font-size: 26px;
    font-weight: 600;
    line-height: 1;
  }
  .firm-of::before, .firm-of::after {
    content: "";
    width: 117px;
    height: 1px;
    background: var(--white);
  }
  .firm-name {
    margin: 18px 0 0;
    font-size: 53px;
    font-weight: 700;
    line-height: 1;
    white-space: nowrap;
  }
  .firm-phone {
    margin-top: 26px;
    font-size: 24px;
    font-weight: 500;
    line-height: 1;
  }
  .cta-panel {
    position: relative;
    width: 232px;
    height: 100%;
  }
  .cta {
    position: absolute;
    left: 0;
    right: 0;
    top: 50px;
    display: flex;
    flex-direction: column;
    align-items: center;
    font-weight: 700;
    text-align: center;
  }
  .cta-question {
    font-size: 24px;
    line-height: 1;
    padding-bottom: 5px;
    border-bottom: 1.5px solid var(--gold-rule);
  }
  .cta-message {
    margin-top: 5px;
    font-size: 30px;
    line-height: 1.2;
  }
  .cta-action {
    margin-top: 2px;
    font-size: 21px;
    color: var(--cta-yellow);
  }
  .award-badge {
    position: absolute;
    left: 163px;
    top: 195px;
    width: 40px;
    height: 58px;
  }
</style>
</head>
<body>
<div class="canvas">
  <div class="billboard">
    <div class="portrait" role="img" aria-label="Black and white portrait of the attorney in a vest and tie, jacket slung over his shoulder"></div>
    <div class="rule-vertical"></div>
    <div class="firm-panel">
      <p class="firm-lead">LAW OFFICES</p>
      <div class="firm-of">OF</div>
      <p class="firm-name">MARTIN G ASHBY</p>
      <div class="firm-phone">(555) 318-4092</div>
    </div>
    <div class="rule-vertical"></div>
    <div class="cta-panel">
      <div class="cta">
        <div class="cta-question">ARRESTED?</div>
        <div class="cta-message">DON’T GO<br>IT ALONE,</div>
        <div class="cta-action">CALL TODAY!</div>
      </div>
      <svg class="award-badge" viewBox="0 0 40 58" aria-hidden="true">
        <rect x="0" y="0" width="40" height="58" fill="var(--badge-blue)"/>
        <rect x="2" y="8" width="36" height="42" fill="var(--badge-dark)"/>
      </svg>
    </div>
  </div>
</div>
</body>
</html>
```